300 x 250 Web Ad for Porn Website

300 x 250 web ad that will appear on a porn site. Need to see 3 options, one with each of the 3 girls. Remove the background around the girls.

Underneath the girls image should read in big bold letters: High Speed Internet
Underneath in slightly smaller size: NO Credit Check

To the left of the girl: Save MONEY...

To the right of the girl: So you can buy more PORN

We want it to look very unique, raunchy, and eye catching.

Target Market(s)

Porn website

Industry/Entity Type

Internet Service Provider

Colors

Designer to choose colors to be used in the design.

Requirements
Must have
• Must stand out so people will definitely notice it.
• JPEG and PNG formats

```html
<!DOCTYPE html>
<html lang="en">
<head>
<meta charset="utf-8">
<title>High Speed Internet – Web Ad Options</title>
<link href="https://fonts.googleapis.com/css2?family=Roboto+Condensed:wght@300;400;700;800&display=swap" rel="stylesheet">
<style>
  :root{
    --page:#ffffff;
    --backdrop-top:#3a5068;
    --backdrop-bottom:#1f2d3c;
    --band:#050a10;
    --accent:#f7ea00;
    --ink-dark:#111111;
    --ink-light:#ffffff;
    --model-light:#b9b9b9;
    --model-dark:#5a5a5a;
  }
  *{box-sizing:border-box;margin:0;padding:0}
  html,body{width:1200px;height:404px;overflow:hidden;background:var(--page)}
  body{position:relative;font-family:"Roboto Condensed",Arial Narrow,sans-serif}
  .ad{
    position:absolute;top:78px;width:300px;height:250px;overflow:hidden;
    background:linear-gradient(180deg,var(--backdrop-top),var(--backdrop-bottom));
  }
  .ad--one{left:87px}
  .ad--two{left:452px}
  .ad--three{left:817px}
  .ad__band{position:absolute;left:0;right:0;top:168px;bottom:0;background:var(--band)}
  .ad__model{position:absolute;top:0;height:250px}
  .ad--one .ad__model{left:0;width:135px}
  .ad--two .ad__model{left:0;width:160px}
  .ad--three .ad__model{left:10px;width:140px}
  .ad__copy{position:absolute;left:150px;width:142px;top:19px;text-align:center;color:var(--ink-light)}
  .ad__tag{
    display:inline-block;background:var(--accent);color:var(--ink-dark);
    font-weight:700;font-size:19px;line-height:31px;padding:0 6px;letter-spacing:-0.3px;
  }
  .ad__line{display:block;font-weight:400;font-size:27px;line-height:30px;letter-spacing:-0.5px;text-transform:uppercase}
  .ad__line:first-of-type{margin-top:3px}
  .ad__punch{display:block;font-weight:800;font-size:44px;line-height:42px;letter-spacing:-1px}
  .ad__private{display:block;margin-top:14px;font-weight:700;font-size:12px;line-height:14px}
  .ad__offer{display:block;color:var(--accent);font-weight:800;font-size:22px;line-height:19px;letter-spacing:-0.3px;margin-top:2px}
  .ad__note{display:block;font-weight:700;font-size:13px;line-height:16px;margin-top:5px}
</style>
</head>
<body>
  <section class="ad ad--one">
    <div class="ad__band"></div>
    <svg class="ad__model" viewBox="0 0 135 250" preserveAspectRatio="none" role="img" aria-label="Black and white cut-out photo of a model in lingerie, seen from behind">
      <defs><linearGradient id="m1" x1="0" y1="0" x2="1" y2="1"><stop offset="0" stop-color="var(--model-light)"/><stop offset="1" stop-color="var(--model-dark)"/></linearGradient></defs>
      <path d="M45 0 H100 Q120 60 130 180 Q135 230 125 250 H0 V70 Q20 20 45 0Z" fill="url(#m1)"/>
    </svg>
    <div class="ad__copy">
      <span class="ad__tag">SAVE MONEY</span>
      <span class="ad__line">So you can</span>
      <span class="ad__line">Buy more</span>
      <span class="ad__punch">PORN!</span>
      <span class="ad__private">100% PRIVATE</span>
      <span class="ad__offer">HIGH SPEED<br>INTERNET</span>
      <span class="ad__note">No Credit Check</span>
    </div>
  </section>

  <section class="ad ad--two">
    <div class="ad__band"></div>
    <svg class="ad__model" viewBox="0 0 160 250" preserveAspectRatio="none" role="img" aria-label="Black and white cut-out photo of a model in lingerie and an open jacket">
      <defs><linearGradient id="m2" x1="0" y1="0" x2="1" y2="1"><stop offset="0" stop-color="var(--model-light)"/><stop offset="1" stop-color="var(--model-dark)"/></linearGradient></defs>
      <path d="M70 0 H115 Q125 60 155 140 Q150 200 130 250 H30 Q10 220 0 160 Q15 100 45 80 Q55 30 70 0Z" fill="url(#m2)"/>
    </svg>
    <div class="ad__copy">
      <span class="ad__tag">SAVE MONEY</span>
      <span class="ad__line">So you can</span>
      <span class="ad__line">Buy more</span>
      <span class="ad__punch">PORN!</span>
      <span class="ad__private">100% PRIVATE</span>
      <span class="ad__offer">HIGH SPEED<br>INTERNET</span>
      <span class="ad__note">No Credit Check</span>
    </div>
  </section>

  <section class="ad ad--three">
    <div class="ad__band"></div>
    <svg class="ad__model" viewBox="0 0 140 250" preserveAspectRatio="none" role="img" aria-label="Black and white cut-out photo of a model in lace lingerie">
      <defs><linearGradient id="m3" x1="0" y1="0" x2="1" y2="1"><stop offset="0" stop-color="var(--model-light)"/><stop offset="1" stop-color="var(--model-dark)"/></linearGradient></defs>
      <path d="M40 10 Q70 -5 100 15 Q115 60 130 110 Q140 190 130 250 H10 Q0 180 5 120 Q20 60 40 10Z" fill="url(#m3)"/>
    </svg>
    <div class="ad__copy">
      <span class="ad__tag">SAVE MONEY</span>
      <span class="ad__line">So you can</span>
      <span class="ad__line">Buy more</span>
      <span class="ad__punch">PORN!</span>
      <span class="ad__private">100% PRIVATE</span>
      <span class="ad__offer">HIGH SPEED<br>INTERNET</span>
      <span class="ad__note">No Credit Check</span>
    </div>
  </section>
</body>
</html>
```